Unique and original Business Card for Financial Services Business

I have moved premises and need to change the detail on my business card so thought now is a good time for a re-design. Looking for something professional and modern with colours to fit in with out logo. Like the idea of foil or embossing if that works but not a must have but I do want something that stands out and that I could not design myself.

Once business card is designed I will also be looking to get letterhead and flyers done but want the business card concept in place first.

The majority of designs I am receiving are generic and template based. I am looking for something unique and original. We have some great design elements in our logo, think outside the box and show me something that stands out from the crowd.

Target Market(s)

Business Professionals

Industry/Entity Type

Finance

Contact Information for Business Card

Name: Delia Norwood Phone 0473 958 162 Address PO Box 8617 Mossvale NSW 2389 Email info@steadyharbourfinancialservices.com.au website www.steadyharbourfinancialservices.com.au

Font styles to use
Other font styles liked:
• Ralway

Requirements
Should not have
• No black backgrounds please

```html
<!DOCTYPE html>
<html lang="en">
<head>
<meta charset="utf-8">
<title>Steady Harbour Financial Services – Business Card</title>
<link rel="stylesheet" href="https://fonts.googleapis.com/css2?family=Raleway:wght@300&family=Montserrat:wght@400;600;700&display=swap">
<style>
  :root {
    --teal-deep: #0b6f86;
    --teal: #13989c;
    --teal-light: #1fa8a6;
    --grey-light: #e4e4e4;
    --grey-mid: #9a9a9a;
    --grey-dark: #6b6b6b;
    --white: #ffffff;
    --paper: #fbfbfb;
    --backdrop: #e8eaeb;
  }
  * { box-sizing: border-box; margin: 0; padding: 0; }
  html, body { width: 1200px; height: 1200px; overflow: hidden; }
  body {
    background: var(--backdrop);
    font-family: "Montserrat", sans-serif;
    position: relative;
  }
  .card {
    position: absolute;
    left: 160px;
    width: 880px;
    height: 536px;
    border-radius: 40px;
    background: linear-gradient(180deg, var(--white), var(--paper));
    overflow: hidden;
    box-shadow: 0 10px 30px rgba(0,0,0,.12);
  }
  .card--front { top: 44px; }
  .card--back { top: 620px; }

  /* Brand name block */
  .brand {
    position: absolute;
    display: flex;
    align-items: center;
    gap: 16px;
    font-family: "Raleway", sans-serif;
    font-weight: 300;
    color: var(--teal-deep);
    white-space: nowrap;
  }
  .brand__dot {
    width: 52px; height: 52px;
    border-radius: 50%;
    background: var(--teal);
    flex: none;
  }
  .brand__text { line-height: 1.1; }
  .brand__name { font-size: 36px; letter-spacing: 1px; text-transform: uppercase; }
  .brand__tag { font-size: 17px; letter-spacing: 8px; }

  .card--front .brand { left: 50%; top: 112px; transform: translateX(-50%); }
  .card--back .brand { left: 48px; top: 226px; }

  /* Front band */
  .stripe {
    position: absolute;
    left: 0; right: 0;
    top: 282px;
    height: 12px;
    background: linear-gradient(90deg, var(--grey-dark), var(--grey-light) 55%, var(--grey-mid));
  }
  .band {
    position: absolute;
    left: 0; right: 0; bottom: 0;
    top: 300px;
    background: linear-gradient(90deg, var(--teal-deep), var(--teal) 70%, var(--teal-light));
  }
  .holder {
    position: absolute;
    left: 60px; bottom: 86px;
    color: var(--white);
    font-weight: 700;
    font-size: 29px;
    letter-spacing: 1.5px;
    text-transform: uppercase;
    white-space: nowrap;
  }
  .contact {
    position: absolute;
    left: 400px; top: 36px;
    list-style: none;
    color: var(--white);
    font-size: 17px;
    white-space: nowrap;
  }
  .contact li {
    display: flex;
    align-items: center;
    gap: 12px;
    height: 38px;
  }
  .contact li:first-child { font-size: 22px; font-weight: 600; }
  .contact svg { width: 20px; height: 20px; flex: none; fill: var(--white); }

  /* Back decoration */
  .back-art {
    position: absolute;
    left: 500px; top: 0; right: 0; bottom: 0;
    background: linear-gradient(135deg, var(--teal) 0%, var(--teal-deep) 45%, var(--grey-mid) 75%, var(--grey-light) 100%);
  }
</style>
</head>
<body>

<section class="card card--front" aria-label="Business card front">
  <div class="brand">
    <span class="brand__dot"></span>
    <div class="brand__text">
      <div class="brand__name">Steady Harbour</div>
      <div class="brand__tag">Financial Services</div>
    </div>
  </div>

  <div class="stripe"></div>
  <div class="band">
    <p class="holder">Delia Norwood</p>
    <ul class="contact">
      <li>
        <svg viewBox="0 0 24 24" aria-hidden="true"><path d="M6.6 10.8a15.1 15.1 0 0 0 6.6 6.6l2.2-2.2a1 1 0 0 1 1-.25 11.4 11.4 0 0 0 3.6.57 1 1 0 0 1 1 1V20a1 1 0 0 1-1 1A17 17 0 0 1 3 4a1 1 0 0 1 1-1h3.5a1 1 0 0 1 1 1c0 1.25.2 2.45.57 3.570a1 1 0 0 1-.25 1z"/></svg>
        0473 958 162
      </li>
      <li>
        <svg viewBox="0 0 24 24" aria-hidden="true"><path fill="none" stroke="#fff" stroke-width="1.8" d="M12 2a10 10 0 1 0 0 20 10 10 0 0 0 0-20zm0 0c3 3 3 17 0 20m0-20c-3 3-3 17 0 20M2 12h20M4 7h16M4 17h16"/></svg>
        www.steadyharbourfinancialservices.com.au
      </li>
      <li>
        <svg viewBox="0 0 24 24" aria-hidden="true"><path d="M2 5h20v14H2z" fill="none" stroke="#fff" stroke-width="1.8"/><path d="M2 5l10 8 10-8" fill="none" stroke="#fff" stroke-width="1.8"/></svg>
        info@steadyharbourfinancialservices.com.au
      </li>
      <li>
        <svg viewBox="0 0 24 24" aria-hidden="true"><path d="M12 2a7 7 0 0 0-7 7c0 5 7 13 7 13s7-8 7-13a7 7 0 0 0-7-7zm0 9.5A2.5 2.5 0 1 1 12 6.5a2.5 2.5 0 0 1 0 5z"/></svg>
        PO Box 8617 Mossvale NSW 2389
      </li>
    </ul>
  </div>
</section>

<section class="card card--back" aria-label="Business card back">
  <div class="brand">
    <span class="brand__dot"></span>
    <div class="brand__text">
      <div class="brand__name">Steady Harbour</div>
      <div class="brand__tag">Financial Services</div>
    </div>
  </div>
  <div class="back-art" role="img" aria-label="Large decorative brand illustration with flourishes in teal and silver"></div>
</section>

</body>
</html>
```